Vireo Halden Business Cards

Vireo Halden Luxury Brand Collection is a global representation business focusing on high end luxury. We need business cards to epitomize our global, luxury delivery model.

Target Market(s)

Global Representation in the hospitality industry

Industry/Entity Type

Hospitality

Contact Information for Business Card

name
title
email: first.last@vh-kmt.com
web: www.vh-kmt.com
mobile:

Requirements
Must have
• double sided design
• incorporate logo colours
• have logo prominent
Should not have
• no designs not incorporating logo colours.

```html
<!DOCTYPE html>
<html lang="en">
<head>
<meta charset="utf-8">
<title>Vireo Halden Business Cards</title>
<link href="https://fonts.googleapis.com/css2?family=Roboto:wght@400;500;700&display=swap" rel="stylesheet">
<style>
  :root {
    --gold: #826c3e;
    --paper: #ffffff;
    --ink: #1c1c1c;
    --stage: #5d6a70;
  }
  * { margin: 0; padding: 0; box-sizing: border-box; }
  html, body { width: 1200px; height: 900px; overflow: hidden; }
  body {
    background: var(--stage);
    position: relative;
    font-family: "Roboto", Arial, sans-serif;
  }
  .card {
    position: absolute;
    width: 560px;
    height: 320px;
    border-radius: 18px;
    overflow: hidden;
    box-shadow: 0 12px 30px rgba(0,0,0,.35);
  }
  /* Back side */
  .card-back {
    left: 80px; top: 100px;
    background: var(--gold);
    display: flex; align-items: center; justify-content: center;
  }
  .back-name {
    font-family: "Roboto", Arial, sans-serif;
    font-weight: 400;
    color: var(--paper);
    font-size: 36px;
    letter-spacing: 2px;
    text-align: center;
  }
  /* Front side */
  .card-front {
    left: 560px; top: 480px;
    background: var(--paper);
  }
  .front-panel { position: absolute; inset: 0; }
  .name-tab {
    position: absolute;
    left: 300px; top: 22px;
    width: 225px; height: 58px;
    background: var(--paper);
    padding: 9px 0 0 34px;
  }
  .person-name {
    font-weight: 700;
    color: var(--gold);
    font-size: 19px;
    letter-spacing: .3px;
  }
  .person-title {
    font-size: 10.5px;
    font-weight: 500;
    color: var(--ink);
    margin-top: 2px;
  }
  .brand {
    position: absolute;
    left: 40px; top: 60px;
    font-family: "Roboto", Arial, sans-serif;
    font-weight: 500;
    font-size: 30px;
    color: var(--gold);
    letter-spacing: .5px;
  }
  .contacts {
    position: absolute;
    left: 40px; top: 186px;
    list-style: none;
  }
  .contact {
    display: flex; align-items: center;
    height: 27px;
    font-size: 14px;
    color: var(--ink);
  }
  .contact-icon {
    width: 20px; height: 20px;
    background: var(--gold);
    margin-right: 12px;
    display: flex; align-items: center; justify-content: center;
  }
  .address {
    position: absolute;
    left: 390px; top: 200px;
    width: 170px;
    color: var(--paper);
    font-size: 13px;
    line-height: 1.35;
    text-align: center;
  }
  .address svg { display: block; margin: 0 auto 6px; }
</style>
</head>
<body>

<section class="card card-back">
  <p class="back-name">Vireo Halden</p>
</section>

<section class="card card-front">
  <svg class="front-panel" width="560" height="320" viewBox="0 0 560 320">
    <polygon points="290,0 560,0 560,320 410,320 352,80 300,80" fill="#826c3e"/>
  </svg>

  <div class="name-tab">
    <p class="person-name">MARLOW PENCE</p>
    <p class="person-title">Founder &amp; Director</p>
  </div>

  <p class="brand">Vireo Halden</p>

  <ul class="contacts">
    <li class="contact">
      <span class="contact-icon"><svg width="12" height="12" viewBox="0 0 24 24"><path fill="#fff" d="M6.6 10.8a15 15 0 0 0 6.6 6.6l2.2-2.2c.3-.3.7-.4 1-.2 1.1.4 2.3.6 3.6.6.6 0 1 .4 1 1V20c0 .6-.4 1-1 1A17 17 0 0 1 3 4c0-.6.4-1 1-1h3.5c.6 0 1 .4 1 1 0 1.2.2 2.4.6 3.6.1.3 0 .7-.2 1z"/></svg></span>
      555-014-2087
    </li>
    <li class="contact">
      <span class="contact-icon"><svg width="12" height="12" viewBox="0 0 24 24"><rect x="3" y="9" width="18" height="12" rx="2" fill="#fff"/><path d="M2 8c3-4 17-4 20 0v2h-5V8H7v2H2z" fill="#fff"/></svg></span>
      555-019-3316
    </li>
    <li class="contact">
      <span class="contact-icon"><svg width="12" height="10" viewBox="0 0 24 18"><rect x="1" y="1" width="22" height="16" fill="none" stroke="#fff" stroke-width="2"/><path d="M1 1l11 9 11-9" fill="none" stroke="#fff" stroke-width="2"/></svg></span>
      first.last@vh-kmt.com
    </li>
    <li class="contact">
      <span class="contact-icon"><svg width="12" height="12" viewBox="0 0 24 24"><circle cx="12" cy="12" r="10" fill="none" stroke="#fff" stroke-width="2"/><ellipse cx="12" cy="12" rx="4" ry="10" fill="none" stroke="#fff" stroke-width="2"/><path d="M2 12h20" stroke="#fff" stroke-width="2"/></svg></span>
      www.vh-kmt.com
    </li>
  </ul>

  <div class="address">
    <svg width="12" height="16" viewBox="0 0 12 16"><path fill="#fff" d="M6 0a6 6 0 0 0-6 6c0 4.5 6 10 6 10s6-5.5 6-10a6 6 0 0 0-6-6zm0 8.5A2.5 2.5 0 1 1 6 3.5a2.5 2.5 0 0 1 0 5z"/></svg>
    88 Larkspur Row - Elmhurst<br>Ferry 40917
  </div>
</section>

</body>
</html>
```